Landing page for a cyber security service provider called 'Lumen Grove'

The client is a new cyber security company in need of a website landing page at lumengrove.example.

Their visual identity is modern, playful, clean and uncluttered and represents innovation, connectivity and approachability.

The company logo is provided in black (attached) but the client is open to changing the colour to align with the new website design.

The landing page needs to contain:
- A call to action with a 'Get Started' button
-Links to blank 'How it works', 'Products', 'Pricing', 'About Us' and 'Contact Us' pages (that we'll fill out later)

Target Market(s)

Medium to large businesses who probably don't understand cyber / cyber security but need their business to be protected.

Industry/Entity Type

Cyber Security

Coding

Coded - Design and coding required

Number of Pages Required

1 page

Font styles to use
Sans Serif
Other font styles liked:
• Helvetica

Requirements
Nice to have
• Hero banner at the top of the landing page.
Should not have
• Should not look like a traditional cyber / cyber security design (eg no dark blue/ black, red/black colour combinations). Please no military styles (eg no shields, cannons, swords, guns)

```html
<!DOCTYPE html>
<html lang="en">
<head>
<meta charset="utf-8">
<title>Lumen Grove — Next-Gen Cybersecurity Made Simple</title>
<link href="https://fonts.googleapis.com/css2?family=Poppins:ital,wght@0,300;0,400;0,500;0,600;1,300&display=swap" rel="stylesheet">
<style>
:root{
  --blue:#0b7be6;
  --blue-soft:#dfe9f7;
  --yellow:#f7c95a;
  --coral:#f07b6c;
  --ink:#2f2f33;
  --text:#555a60;
  --muted:#7a7f86;
  --bg:#f7f9fc;
  --white:#ffffff;
}
*{box-sizing:border-box;margin:0;padding:0}
html,body{width:1200px;height:3525px;overflow:hidden}
body{position:relative;font-family:"Poppins",sans-serif;color:var(--ink);
  background:radial-gradient(circle at 20% 10%,#eef3fb 0,transparent 40%),radial-gradient(circle at 80% 45%,#eef3fb 0,transparent 35%),radial-gradient(circle at 30% 85%,#eef3fb 0,transparent 35%),var(--bg)}
.abs{position:absolute}
a{text-decoration:none;color:inherit}
.btn{display:inline-flex;align-items:center;justify-content:center;background:var(--blue);color:var(--white);font-weight:600;font-size:14px;border-radius:6px;box-shadow:0 4px 10px rgba(11,123,230,.25)}
.brand{font-weight:600;font-size:24px;line-height:30px;color:var(--ink);display:flex;align-items:center;gap:10px}
.brand .dot{width:18px;height:18px;border-radius:50%;background:var(--ink)}
.nav{top:36px;left:654px;display:flex;gap:24px;font-size:14px;color:var(--text);line-height:22px}
.section-title{width:100%;text-align:center;font-weight:600;font-size:46px;line-height:57px;color:var(--ink)}
.lead{width:100%;text-align:center;font-size:18px;line-height:30px;color:var(--text)}
.hero-title{top:117px;width:100%;text-align:center;font-size:46px;line-height:58px;font-weight:600}
.hero-title span{color:var(--blue)}
.illus{border-radius:18px}
.step{width:306px;height:492px;background:var(--white);border-radius:8px;box-shadow:0 6px 18px rgba(40,60,100,.08);padding:28px 18px 0 34px;overflow:hidden}
.step::before{content:"";position:absolute;left:0;top:0;bottom:0;width:7px;background:var(--c)}
.step .num{font-size:24px;font-weight:500;position:relative}
.step .num::after{content:"";position:absolute;left:18px;top:4px;width:32px;height:32px;border-radius:50%;background:var(--c);opacity:.2}
.step h3{font-size:18px;font-weight:600;line-height:28px;margin-top:16px}
.step p{font-size:14.5px;line-height:27.5px;color:var(--text);margin-top:6px}
.step .art{position:absolute;left:40px;right:20px;bottom:0;height:170px;border-radius:8px 8px 0 0}
.toggle{height:44px;border-radius:6px;font-size:14px;font-weight:500;display:flex;align-items:center;justify-content:center}
.plan{width:254px;height:445px;background:var(--white);border-radius:8px;box-shadow:0 6px 18px rgba(40,60,100,.08);text-align:center;border-bottom:7px solid var(--c);padding-top:34px}
.plan h4{font-size:20px;font-weight:400}
.price{margin-top:14px;display:flex;align-items:center;justify-content:center;gap:12px}
.price small{font-size:13px;color:var(--text)}
.price strong{font-size:42px;font-weight:600}
.plan .tag{font-size:13px;color:var(--text);margin-top:8px}
.plan .rule{width:46px;height:3px;background:var(--blue);margin:20px auto 26px}
.plan ul{list-style:none;font-size:13px;line-height:26px;color:var(--text)}
.plan .btn{width:170px;height:42px;margin-top:26px}
.testimonial{top:2700px;left:112px;width:976px;height:352px;background:var(--white);border-radius:8px;box-shadow:0 6px 18px rgba(40,60,100,.08);border-bottom:8px solid var(--yellow);text-align:center;padding-top:100px}
.stars{color:var(--yellow);font-size:18px;letter-spacing:2px}
.quote{font-style:italic;font-weight:300;font-size:16px;line-height:30px;color:var(--text);width:750px;margin:10px auto 0}
.author{margin-top:22px;font-size:16px;color:var(--text)}
.author b{font-weight:600;color:var(--ink)}
.footer-col h5{color:var(--blue);font-size:16px;font-weight:600;letter-spacing:.5px;margin-bottom:10px}
.footer-col li{list-style:none;font-size:15px;line-height:26px;color:var(--text)}
.contact li{display:flex;gap:14px;align-items:flex-start;margin-bottom:6px}
.contact svg{flex:none;margin-top:5px}
.social{display:flex;gap:8px}
.social span{width:32px;height:32px;border:1.5px solid var(--ink);border-radius:50%}
</style>
</head>
<body>

<!-- Header -->
<a class="abs brand" href="#" style="top:50px;left:115px"><span class="dot"></span><span>Lumen Grove</span></a>
<nav class="abs nav"><a href="#">How it works</a><a href="#">Pricing</a><a href="#">About Us</a></nav>
<a class="abs btn" href="#" style="top:25px;left:941px;width:148px;height:44px">GET STARTED</a>

<!-- Hero -->
<h1 class="abs hero-title"><span>Next-Gen</span> Cybersecurity<br>Made Simple</h1>
<p class="abs lead" style="top:243px;font-size:17px">Protect Your Business with Proactive Cyber Defence Solutions –<br>No Expertise Required</p>
<a class="abs btn" href="#" style="top:331px;left:526px;width:148px;height:44px">GET STARTED</a>
<div class="abs illus" role="img" aria-label="Illustration of a team working at desks in a bright modern office" style="top:375px;left:112px;width:976px;height:258px;background:linear-gradient(90deg,rgba(240,164,90,.18),rgba(11,123,230,.12) 55%,#c9dbf4 70%,#dbe6f6)"></div>

<!-- How it works -->
<h2 class="abs section-title" style="top:730px">How It Works</h2>
<p class="abs lead" style="top:796px">Lorem ipsum dolor sit amet, consectetur adipiscing elit, sed do eiusmod<br>tempor incididunt ut labore et dolore magna aliqua.</p>

<article class="abs step" style="top:917px;left:112px;--c:var(--blue)">
  <div class="num">01</div>
  <h3>Comprehensive Threat<br>Detection</h3>
  <p>Lorem ipsum dolmt, consectetur<br>adipiscing elit, sed do eiusmod<br>tempor incididunt ut labore et<br>dolore magna aliqua. Quis ipsum<br>suspendisse ultrices gravida.</p>
  <div class="art" role="img" aria-label="Illustration of a person at a laptop with a padlock and data panels" style="background:linear-gradient(160deg,#dde8f8,#f6f0df)"></div>
</article>
<article class="abs step" style="top:917px;left:447px;--c:var(--yellow)">
  <div class="num">02</div>
  <h3>Simplified Security<br>Management</h3>
  <p>Lorem ipsum dolmt, consectetur<br>adipiscing elit, sed do eiusmod<br>tempor incididunt ut labore et<br>dolore magna aliqua. Quis ipsum<br>suspendisse ultrices gravida.</p>
  <div class="art" role="img" aria-label="Illustration of two people reviewing dashboards on large monitors" style="background:linear-gradient(160deg,#d6e4f7,#fbeccd)"></div>
</article>
<article class="abs step" style="top:917px;left:782px;--c:var(--coral)">
  <div class="num">03</div>
  <h3>Automated Incident<br>Response</h3>
  <p>Lorem ipsum dolmt, consectetur<br>adipiscing elit, sed do eiusmod<br>tempor incididunt ut labore et<br>dolore magna aliqua. Quis ipsum<br>suspendisse ultrices gravida.</p>
  <div class="art" role="img" aria-label="Illustration of a laptop with a padlock, cloud and connected files" style="background:linear-gradient(160deg,#e7eef8,#dce8f7)"></div>
</article>

<a class="abs btn" href="#" style="top:1461px;left:526px;width:148px;height:44px">VIEW MORE</a>

<!-- Pricing -->
<h2 class="abs section-title" style="top:1627px">Choose the Right Plan<br>for Your Needs</h2>
<p class="abs lead" style="top:1758px">Lorem ipsum dolor sit amet, consectetur adipiscing elit, sed do eiusmod<br>tempor incididunt ut labore et dolore magna aliqua.</p>
<a class="abs toggle" href="#" style="top:1855px;left:445px;width:148px;background:var(--blue-soft);color:var(--blue)">PAY MONTHLY</a>
<a class="abs toggle btn" href="#" style="top:1855px;left:608px;width:148px">PAY YEARLY</a>

<div class="abs plan" style="top:1957px;left:173px;--c:var(--blue)">
  <h4>Basic Plan</h4>
  <div class="price"><small>from</small><strong>$95</strong></div>
  <div class="tag">Lorem Ipsum Set Amit</div><div class="rule"></div>
  <ul><li>Sed ut perspiciatis</li><li>Unde omnis iste natus error sit</li><li>Voluptatem accusantium dolorem</li><li>Que laudantium, totam rem</li><li>Aperiam, eaque ipsa quae ab illo</li></ul>
  <a class="btn" href="#">GET STARTED</a>
</div>
<div class="abs plan" style="top:1957px;left:473px;--c:var(--yellow)">
  <h4>Basic Plan</h4>
  <div class="price"><small>from</small><strong>$105</strong></div>
  <div class="tag">Lorem Ipsum Set Amit</div><div class="rule"></div>
  <ul><li>Sed ut perspiciatis</li><li>Unde omnis iste natus error sit</li><li>Voluptatem accusantium dolorem</li><li>Que laudantium, totam rem</li><li>Aperiam, eaque ipsa quae ab illo</li></ul>
  <a class="btn" href="#">GET STARTED</a>
</div>
<div class="abs plan" style="top:1957px;left:773px;--c:var(--coral)">
  <h4>Basic Plan</h4>
  <div class="price"><small>from</small><strong>$125</strong></div>
  <div class="tag">Lorem Ipsum Set Amit</div><div class="rule"></div>
  <ul><li>Sed ut perspiciatis</li><li>Unde omnis iste natus error sit</li><li>Voluptatem accusantium dolorem</li><li>Que laudantium, totam rem</li><li>Aperiam, eaque ipsa quae ab illo</li></ul>
  <a class="btn" href="#">GET STARTED</a>
</div>

<!-- Testimonials -->
<h2 class="abs section-title" style="top:2546px">Client Testimonials</h2>
<div class="abs testimonial">
  <div class="stars">★★★★★</div>
  <p class="quote">Lorem ipsum dolor sit ametctetur adipiscinelit, sed do eiusmod tempor incididunt ut labore et dolore magna aliqua. Ut enim ad minim veniam, quis nostrud exercitation ullamco laborisnisi ut aliquip ex ea commodo cquat. Duis aute irure dolor in rehenderit in voluptateelit esse cillum dolore eu fugiat nulla pariatur.</p>
  <p class="author"><b>Mara Ellison</b>, CEO Lorem Ipsum</p>
</div>
<div class="abs" role="img" aria-label="Client portrait" style="top:2654px;left:547px;width:106px;height:106px;border-radius:50%;background:linear-gradient(160deg,#f6d3c5,#b9d3ef);border:4px solid #dce8f6"></div>
<svg class="abs" style="top:2866px;left:143px" width="32" height="20" viewBox="0 0 32 20" aria-label="Previous"><path d="M30 10H3M11 2 3 10l8 8" fill="none" stroke="var(--blue)" stroke-width="2.5" stroke-linecap="round" stroke-linejoin="round"/></svg>
<svg class="abs" style="top:2866px;left:1028px" width="32" height="20" viewBox="0 0 32 20" aria-label="Next"><path d="M2 10h27M21 2l8 8-8 8" fill="none" stroke="var(--blue)" stroke-width="2.5" stroke-linecap="round" stroke-linejoin="round"/></svg>

<!-- Footer -->
<a class="abs brand" href="#" style="top:3320px;left:112px"><span class="dot"></span><span>Lumen Grove</span></a>
<div class="abs footer-col" style="top:3255px;left:373px">
  <h5>QUICK LINKS</h5>
  <ul><li>How it works</li><li>Pricing</li><li>About Us</li></ul>
</div>
<div class="abs footer-col" style="top:3255px;left:604px">
  <h5>QUICK LINKS</h5>
  <ul><li>Contact Us</li><li>Terms &amp; Conditions</li><li>Privacy Policy</li></ul>
</div>
<div class="abs footer-col contact" style="top:3255px;left:889px">
  <h5>CONTACT US</h5>
  <ul>
    <li><svg width="14" height="16" viewBox="0 0 14 18"><path d="M7 0a7 7 0 0 0-7 7c0 5 7 11 7 11s7-6 7-11a7 7 0 0 0-7-7zm0 10a3 3 0 1 1 0-6 3 3 0 0 1 0 6z" fill="var(--ink)"/></svg><span>Lumen Grove,<br>Address Comes Here</span></li>
    <li><svg width="14" height="14" viewBox="0 0 16 16"><path d="M3 1l3 3-2 2c1 2 3 4 5 5l2-2 3 3-2 3C7 15 1 9 0 3z" fill="var(--ink)"/></svg><span>+1 555-010-0199</span></li>
    <li><svg width="15" height="12" viewBox="0 0 16 12"><path d="M0 0h16v12H0z" fill="var(--ink)"/><path d="M1 1l7 6 7-6" fill="none" stroke="#fff" stroke-width="1.3"/></svg><span>info@lumengrove.example</span></li>
  </ul>
</div>
<div class="abs" style="top:3452px;left:112px;width:976px;height:1px;background:#d9dde3"></div>
<p class="abs" style="top:3480px;left:112px;font-size:15px;color:var(--text)">2024 Lumen Grove. All Rights Reserved.</p>
<div class="abs social" style="top:3474px;left:903px" aria-label="Social media links"><span></span><span></span><span></span><span></span><span></span></div>

</body>
</html>
```